Car Repair Business Website Redesign

We need a new design for our wordpress website, which generates traffic and converts leads for our car repair business. The site was originally setup with a blank template and the design was never tweaked. All content is in place, so the design needs to arrange existing content into a visually strong, responsive layout with top priority given to conversion. You can view the existing website at www.brightlanegarageworks.com. Responsive design is extremely important - 36% of visitors are mobile and 18% tablet - so please include mobile designs.
To confirm, the brief is for PSD only, please supply designs for the following two pages:-
http://www.brightlanegarageworks.com/
http://www.brightlanegarageworks.com/clutch-replacement/
Target Market(s)
Predominantly male (75%), 25-55 year old (70%) audience.
Industry/Entity Type
Car Repair
Number of Pages Required
2 page
Font styles to use
Requirements
Must have
- Good use of colour, clear design elements. Our competitors just had a re-design which although not perfect, displays many good elements: www.gearvalet.com

```html
<!DOCTYPE html>
<html lang="en">
<head>
<meta charset="utf-8">
<title>Brightlane Garageworks</title>
<link href="https://fonts.googleapis.com/css2?family=Lato:wght@400;700&family=PT+Sans:wght@400;700&display=swap" rel="stylesheet">
<style>
:root{
  --blue:#0a6fb0;
  --ink:#222;
  --line:#d6d6d6;
  --footer:#3a3a3a;
  --footer-bar:#2b2b2b;
  --white:#fff;
  --hero-top:#3a3b3e;
  --hero-bottom:#1a1b1d;
  --art:#d9d9d9;
}
*{box-sizing:border-box;margin:0;padding:0}
html,body{width:751px;height:1200px;overflow:hidden;background:var(--white);font-family:"Lato",sans-serif;color:var(--ink)}
.page{position:relative;width:751px;height:1200px}
.abs{position:absolute}

/* header */
.site-header{left:0;top:0;width:751px;height:56px;border-bottom:1px solid #ddd;background:var(--white)}
.brand{position:absolute;left:116px;top:20px;display:flex;align-items:center;gap:6px}
.brand-mark{width:11px;height:11px;background:var(--blue);border-radius:50%}
.brand-name{font-family:"PT Sans",sans-serif;font-weight:700;font-size:13px;color:#1a1a1a}
.main-nav{left:313px;top:33px;display:flex;gap:22px;font-size:8px}
.main-nav a{color:#222;text-decoration:none;position:relative}
.main-nav a.active{color:var(--blue)}
.main-nav a.active::before{content:"";position:absolute;left:-1px;right:-1px;top:-7px;height:2px;background:var(--blue)}
.social{left:573px;top:7px;display:flex;gap:13px}
.social span{width:12px;height:12px;border-radius:2px;background:#1f7cc4}
.phone{left:550px;top:27px;font-size:12.5px;color:#8a8a8a;text-align:center;width:88px}
.phone small{display:block;font-size:7px}

/* hero */
.hero{left:0;top:56px;width:751px;height:320px;background:linear-gradient(180deg,var(--hero-top),var(--hero-bottom))}

/* services */
.service{top:438px;width:120px;height:102px;border:1px solid #ddd;border-top:none;box-shadow:0 1px 2px rgba(0,0,0,.12);text-align:center}
.service .art{position:absolute;left:35px;top:-22px;width:50px;height:46px;background:var(--art)}
.service h3{font-family:"PT Sans",sans-serif;font-weight:400;font-size:10px;margin-top:35px}
.service p{font-size:6.2px;line-height:9.7px;color:#333;padding:0 6px;margin-top:5px}

/* cta */
.cta{left:114px;top:566px;width:520px;height:58px;background:var(--blue);text-align:center;color:var(--white)}
.cta h2{font-family:"PT Sans",sans-serif;font-size:12.5px;margin-top:7px}
.cta p{font-size:6px;margin-top:4px}
.cta a{display:inline-block;margin-top:5px;background:#1d3343;color:var(--white);font-size:6px;padding:3px 9px;text-decoration:none}
.cta-shadow{left:80px;top:624px;width:590px;height:16px;background:radial-gradient(ellipse at 50% 0,rgba(0,0,0,.28),rgba(0,0,0,0) 70%)}

/* section heads */
.sec-title{font-family:"PT Sans",sans-serif;font-size:12.5px;color:var(--blue);font-weight:400}
.sec-rule{height:1px;background:var(--line);position:relative;margin-top:7px}
.sec-rule::before{content:"";position:absolute;left:0;top:-1px;width:28px;height:2px;background:var(--blue)}

/* faq */
.faq{left:115px;top:656px;width:253px}
.faq-list{margin-top:10px;list-style:none}
.faq-list li{display:flex;align-items:center;justify-content:space-between;height:21px;border-bottom:1px solid #cfcfcf;font-size:7px}
.faq-list .toggle{width:15px;height:14px;background:var(--blue);color:var(--white);font-size:9px;line-height:13px;text-align:center}
.faq-answer{font-size:6.5px;line-height:10.5px;color:#888;padding:5px 40px 4px 0}

/* why */
.why{left:384px;top:656px;width:252px}
.why-list{margin-top:12px;list-style:none;width:252px}
.why-list li{font-size:6.2px;line-height:10px;color:var(--blue);padding:0 0 4px 1px;border-bottom:1px solid #e2e2e2;margin-bottom:4px}
.divider{left:114px;top:882px;width:521px;height:1px;background:#ddd}

/* reviews */
.reviews{left:116px;top:893px;width:252px}
.reviews .arrows{position:absolute;right:0;top:1px;display:flex;gap:6px}
.review-box{left:115px;top:918px;width:254px;height:72px;border:1px solid #d4d4d4;background:#f6f6f6}
.avatar{position:absolute;left:5px;top:8px;width:42px;height:42px;border-radius:50%;border:2px solid #ddd;background:#c9c2bc}
.review-box p{position:absolute;left:52px;top:8px;width:196px;font-size:6.2px;line-height:12px;font-style:italic;color:#555}
.review-box a{position:absolute;right:13px;top:56px;font-size:7px;font-style:italic;color:var(--blue)}

/* help */
.help{left:383px;top:893px;width:253px}
.help-box{left:382px;top:918px;width:254px;height:72px;border:1px solid #d4d4d4;display:flex;justify-content:space-around;align-items:center;text-align:center}
.help-item{font-size:8.4px;color:var(--blue)}
.help-item svg{display:block;margin:0 auto 6px}

/* footer */
.site-footer{left:0;top:1010px;width:751px;height:148px;background:var(--footer);color:var(--white)}
.foot-title{font-size:8.5px;font-weight:700;text-transform:uppercase}
.contact{left:115px;top:25px;width:130px}
.contact-item{display:flex;gap:5px;font-size:6.4px;font-weight:700;line-height:11px;margin-top:12px}
.branch{left:249px;top:25px;width:133px}
.search{margin-top:9px;height:19px;background:var(--white);color:#888;font-size:8.5px;padding:3px 6px;display:flex;justify-content:space-between;align-items:center}
.addr{font-size:7.2px;line-height:11.5px;color:#eee;padding:6px 0 4px;border-bottom:1px solid #555}
.map{left:414px;top:29px;width:222px;height:103px;background:linear-gradient(135deg,#dfe6d6,#c9d8c0 60%,#a9c4d8)}
.foot-bar{left:0;top:1158px;width:751px;height:42px;background:var(--footer-bar);color:var(--white);font-size:6.5px}
.foot-bar .copy{position:absolute;left:103px;top:16px}
.foot-bar .links{position:absolute;right:115px;top:16px;display:flex;gap:12px;font-weight:700}
</style>
</head>
<body>
<div class="page">

  <header class="site-header abs">
    <div class="brand"><span class="brand-mark"></span><span class="brand-name">Brightlane Garageworks</span></div>
    <nav class="main-nav abs">
      <a class="active" href="#">Home</a><a href="#">Service</a><a href="#">Location</a><a href="#">FAQ</a><a href="#">About Us</a>
    </nav>
    <div class="social abs"><span></span><span></span><span></span></div>
    <div class="phone abs">0800 555 0142<small>(Toll Free)</small></div>
  </header>

  <div class="hero abs" role="img" aria-label="Photograph of an open car bonnet showing the engine bay"></div>

  <article class="service abs" style="left:115px">
    <div class="art" role="img" aria-label="Clutch kit image"></div>
    <h3>Clutch Replacement</h3>
    <p>Clutch Replacement – As clutch specialists replacing hundreds of clutches every month, we offer convenience, reliability and value.</p>
  </article>
  <article class="service abs" style="left:248px">
    <div class="art" role="img" aria-label="Cambelt image"></div>
    <h3>Cambelt Replacement</h3>
    <p>Clutch Replacement – As clutch specialists replacing hundreds of clutches every month, we offer convenience, reliability and value.</p>
  </article>
  <article class="service abs" style="left:382px">
    <div class="art" role="img" aria-label="Wheel and tools image"></div>
    <h3>Servicing</h3>
    <p>Clutch Replacement – As clutch specialists replacing hundreds of clutches every month, we offer convenience, reliability and value.</p>
  </article>
  <article class="service abs" style="left:515px">
    <div class="art" role="img" aria-label="Brake disc and pad image"></div>
    <h3>Brake Discs &amp; Pads</h3>
    <p>Clutch Replacement – As clutch specialists replacing hundreds of clutches every month, we offer convenience, reliability and value.</p>
  </article>

  <section class="cta abs">
    <h2>Do I Need a Clutch Replacement?</h2>
    <p>Just answer a few basic questions to diagnose your clutch problem with our interactive clutch troubleshooter!</p>
    <a href="#">Know More</a>
  </section>
  <div class="cta-shadow abs"></div>

  <section class="faq abs">
    <h2 class="sec-title">Clutch Frequently Asked Questions</h2>
    <div class="sec-rule" style="width:210px"></div>
    <ul class="faq-list">
      <li>How do I know if I need a Clutch Replacement?<span class="toggle">–</span></li>
      <li style="border-bottom:none">How quickly can you get my car booked in for a clutch replacement?<span class="toggle">+</span></li>
      <li style="display:block;height:auto;border-bottom:none"><div class="faq-answer">We often have last minute availability for urgent repairs - just get in touch and we'll let you know.</div></li>
      <li>How long does it take to get my clutch repaired?<span class="toggle">–</span></li>
      <li>There is further work required on my vehicle, are you able to help?<span class="toggle">–</span></li>
      <li>My car is an automatic, is it fitted with a clutch?<span class="toggle">–</span></li>
      <li>How can I pay for my clutch repair?<span class="toggle">–</span></li>
      <li>How does the warranty work?<span class="toggle">–</span></li>
    </ul>
  </section>

  <section class="why abs">
    <h2 class="sec-title">Why We Are The Best Choice</h2>
    <div class="sec-rule" style="width:210px"></div>
    <ul class="why-list">
      <li>Lorem Ipsum is simply dummy text of the printing and typesetting industry. Lorem Ipsum has been the industry's standard dummy text ever since the 1500s, when an unknown printer took</li>
      <li>Lorem Ipsum is simply dummy text of the printing and typesetting industry. Lorem Ipsum has been the industry's standard dummy text ever since the 1500s, when an unknown printer took</li>
      <li>Lorem Ipsum is simply dummy text of the printing and typesetting industry. Lorem Ipsum has been the industry's standard dummy text ever since the 1500s, when an unknown printer took</li>
      <li>Lorem Ipsum is simply dummy text of the printing and typesetting industry. Lorem Ipsum has been the industry's standard dummy text ever since the 1500s, when an unknown printer took</li>
      <li style="border:none;width:235px">Lorem Ipsum is simply dummy text of the printing and typesetting industry. Lorem Ipsum has been the industry's standard dummy text ever since the 1500s, when an unknown printer took</li>
    </ul>
  </section>

  <div class="divider abs"></div>

  <section class="reviews abs">
    <h2 class="sec-title">Preview Castomers Reviews</h2>
    <div class="arrows">
      <svg width="7" height="10" viewBox="0 0 7 10"><path d="M6 1 2 5l4 4" fill="none" stroke="#0a6fb0" stroke-width="2"/></svg>
      <svg width="7" height="10" viewBox="0 0 7 10"><path d="M1 1l4 4-4 4" fill="none" stroke="#0a6fb0" stroke-width="2"/></svg>
    </div>
  </section>
  <div class="review-box abs">
    <div class="avatar" role="img" aria-label="Customer portrait photo"></div>
    <p>It is a long established fact that a reader will be distracted by the readable content of a page when looking at its layout. The point of using Lorem Ipsum is that it has a more-or-less normal distribution of letters, as opposed to using</p>
    <a href="#">Read More</a>
  </div>

  <section class="help abs"><h2 class="sec-title">Need A Help?</h2></section>
  <div class="help-box abs">
    <div class="help-item">
      <svg width="30" height="24" viewBox="0 0 30 24"><ellipse cx="11" cy="9" rx="10" ry="8" fill="#0a6fb0"/><path d="M5 15l-2 5 6-3z" fill="#0a6fb0"/><ellipse cx="20" cy="14" rx="9" ry="7" fill="#0a6fb0" stroke="#fff" stroke-width="1.5"/><circle cx="16" cy="14" r="1.2" fill="#fff"/><circle cx="20" cy="14" r="1.2" fill="#fff"/><circle cx="24" cy="14" r="1.2" fill="#fff"/></svg>
      Chat With Us</div>
    <div class="help-item">
      <svg width="24" height="24" viewBox="0 0 24 24"><rect width="24" height="24" rx="4" fill="#0a6fb0"/><path d="M8 5c-2 1-2 4 0 7s5 6 8 7c2 0 3-2 2-3l-2-2-2 1c-2-1-4-3-5-5l1-2-2-3z" fill="#fff"/></svg>
      Request A Callback</div>
    <div class="help-item">
      <svg width="26" height="24" viewBox="0 0 26 24"><ellipse cx="13" cy="10" rx="12" ry="9" fill="#0a6fb0"/><path d="M5 16l-3 7 8-5z" fill="#0a6fb0"/><path d="M8 8h4v3l-2 4H8l1-3H8zM14 8h4v3l-2 4h-2l1-3h-1z" fill="#fff"/></svg>
      Ask For A Quote</div>
  </div>

  <footer class="site-footer abs">
    <div class="contact abs">
      <h3 class="foot-title">Contact Us</h3>
      <div class="contact-item">
        <svg width="9" height="9" viewBox="0 0 9 9"><rect width="9" height="9" rx="1.5" fill="#fff"/><path d="M3 2c-1 .5-1 1.5 0 3s2 2 3 2.3c.7 0 1-.7.7-1L6 5.6l-.7.3C4.6 5.6 4 5 3.6 4.3L4 3.6z" fill="#3a3a3a"/></svg>
        <span>Need Advice? Got a Question?<br>Call us on 0800 555 0142</span></div>
      <div class="contact-item">
        <svg width="9" height="7" viewBox="0 0 9 7"><rect width="9" height="7" fill="#fff"/><path d="M0 0l4.5 4L9 0" fill="none" stroke="#3a3a3a"/></svg>
        <span>You can also email us at:<br>info@brightlanegarageworks.com</span></div>
    </div>
    <div class="branch abs">
      <h3 class="foot-title">Find Your Closest Branch</h3>
      <div class="search">City/Post Code
        <svg width="9" height="9" viewBox="0 0 9 9"><circle cx="3.7" cy="3.7" r="2.8" fill="none" stroke="#888" stroke-width="1.3"/><path d="M6 6l2.5 2.5" stroke="#888" stroke-width="1.4"/></svg></div>
      <div class="addr">27, mkbhdkjj kdfjkjkldfs kfjdkfj dfjkdfjkldfs jdfhdfsk, 52126</div>
      <div class="addr" style="border:none">27, mkbhdkjj kdfjkjkldfs kfjdkfj dfjkdfjkldfs jdfhdfsk, 52126</div>
    </div>
    <div class="map abs" role="img" aria-label="Map of southern England marking branch locations"></div>
  </footer>

  <div class="foot-bar abs">
    <span class="copy">© 2015 Brightlane Garageworks All Rights Reserved</span>
    <div class="links"><span>✆ 0800 555 0142</span><span>✉ info@brightlanegarageworks.com</span></div>
  </div>

</div>
</body>
</html>
```